Personal Letterhead - Vintage / Antique - Foil Pressed

I need a personal letterhead. I'm an engineer and maker who enjoys writing letters and calligraphy. The final design will be foil pressed with either gold or copper foil. I'm going for an antique and vintage look. Something akin to Walter Brisbane's letterhead. Please include a spot for a web address and email, each are 16 characters long. The primary name to include is Daniel Harper. You can include print elements if desired that will be separate from the foil elements. At your discretion, you may or may not include the Harper signature I attached. It is optional depending on how well it meshes with your design.
I, explicitly, am not just looking for my name in gold or copper at the top of the page. I'm looking for additional design elements that give a similar feeling to the example design provided.

```html
<!DOCTYPE html>
<html lang="en">
<head>
<meta charset="utf-8">
<title>Daniel Harper — Personal Letterhead</title>
<link href="https://fonts.googleapis.com/css2?family=Cinzel:wght@600;900&family=Dancing+Script:wght@500&family=Libre+Baskerville:wght@700&display=swap" rel="stylesheet">
<style>
  :root {
    --page-bg: #ffffff;
    --paper: #ebe3d0;
    --ink: #3b3327;
    --foil: #d9740f;
    --stamp-grey: #7d7d77;
    --stamp-brown: #9a8d80;
  }
  html, body {
    margin: 0;
    padding: 0;
    width: 1000px;
    height: 1200px;
    overflow: hidden;
    background: var(--page-bg);
  }
  .canvas {
    position: relative;
    width: 1000px;
    height: 1200px;
  }
  .sheet {
    position: absolute;
    left: 95px;
    top: 75px;
    width: 810px;
    height: 1050px;
    background: var(--paper);
  }
  .artwork {
    position: absolute;
    inset: 0;
    width: 1000px;
    height: 1200px;
  }
  .dept-label {
    font-family: "Cinzel", serif;
    font-weight: 600;
    font-size: 17px;
    fill: var(--ink);
  }
  .masthead-name {
    font-family: "Cinzel", serif;
    font-weight: 900;
    font-size: 40px;
    fill: var(--foil);
  }
  .footer-name {
    font-family: "Libre Baskerville", serif;
    font-weight: 700;
    font-size: 13px;
    letter-spacing: 3px;
    fill: var(--ink);
  }
  .contact {
    font-family: "Libre Baskerville", serif;
    font-weight: 700;
    font-size: 15px;
    fill: var(--ink);
  }
  .letter {
    position: absolute;
    left: 158px;
    top: 306px;
    width: 690px;
    font-family: "Dancing Script", cursive;
    font-weight: 500;
    color: var(--ink);
    font-size: 26px;
    white-space: nowrap;
  }
  .letter p { margin: 0; line-height: 48px; }
  .letter .meta { line-height: 32px; margin-bottom: 22px; }
  .letter .body { margin-bottom: 15px; }
  .letter .indent { padding-left: 47px; }
  .printed-name {
    position: absolute;
    left: 398px;
    top: 890px;
    font-family: "Dancing Script", cursive;
    font-size: 17px;
    color: var(--ink);
  }
</style>
</head>
<body>
<div class="canvas">
  <div class="sheet"></div>

  <svg class="artwork" viewBox="0 0 1000 1200" xmlns="http://www.w3.org/2000/svg">
    <!-- masthead: plain double frame with rules -->
    <g class="masthead-frame" fill="none" stroke="var(--ink)" stroke-width="2">
      <rect x="208" y="168" width="584" height="100"/>
      <rect x="215" y="175" width="570" height="86"/>
      <path d="M300 200 H700"/>
      <path d="M500 268 V312 M493 312 H507"/>
    </g>
    <text class="dept-label" x="500" y="193" text-anchor="middle" textLength="370" lengthAdjust="spacing">ENGINEERING DEPARTMENT</text>
    <text class="masthead-name" x="497" y="245" text-anchor="middle" textLength="525" lengthAdjust="spacing">DANIEL HARPER</text>

    <!-- postage marks -->
    <g role="img" aria-label="Faded New York postmark">
      <circle cx="685" cy="335" r="31" fill="var(--stamp-brown)" opacity="0.4"/>
      <path d="M716 322 H760 M716 335 H760 M716 348 H760" stroke="var(--stamp-brown)" stroke-width="4" opacity="0.4"/>
    </g>
    <g role="img" aria-label="San Francisco bridge postmark">
      <circle cx="808" cy="338" r="52" fill="var(--stamp-brown)" opacity="0.5"/>
    </g>
    <g role="img" aria-label="London letter express postage stamp" transform="rotate(-6 203 888)">
      <rect x="127" y="845" width="152" height="86" fill="var(--stamp-grey)"/>
    </g>

    <!-- signature -->
    <g role="img" aria-label="Handwritten signature of Daniel Harper">
      <rect x="325" y="790" width="380" height="95" rx="40" fill="var(--ink)" opacity="0.1"/>
    </g>

    <!-- footer: plain boxes and rules -->
    <g class="footer-lines" fill="none" stroke="var(--ink)" stroke-width="2">
      <path d="M500 918 V943 M494 918 H506"/>
      <path d="M267 960 H385 M618 960 H735"/>
      <rect x="385" y="943" width="233" height="32" fill="var(--paper)"/>
      <rect x="158" y="989" width="272" height="28" fill="var(--paper)"/>
      <rect x="568" y="989" width="275" height="28" fill="var(--paper)"/>
      <path d="M500 975 V990 M500 1062 V1072 M494 1072 H506"/>
    </g>
    <g role="img" aria-label="Handwritten monogram initials">
      <rect x="474" y="992" width="48" height="70" rx="20" fill="var(--ink)" opacity="0.1"/>
    </g>
    <text class="footer-name" x="501" y="965" text-anchor="middle">DANIEL HARPER</text>
    <text class="contact" x="294" y="1008" text-anchor="middle">username@email.com</text>
    <text class="contact" x="705" y="1008" text-anchor="middle">www.yourwebsite.com</text>
  </svg>

  <div class="letter">
    <p class="meta">Month Day, Year<br>Salutation;</p>
    <p class="body"><span class="indent">Lorem ipsum dolor sit amet, consectetuer adipiscing elit.</span><br>Aenean commodo ligula eget dolor. Aenean massa. Cum sociis<br>natoque penatibus et magnis dis parturient montes, nascetur<br>ridiculus mus. Donec quam felis, ultricies nec, pellentesque eu,<br>pretium quis, sem.</p>
    <p class="body"><span class="indent">Integer tincidunt. Cras dapibus. Vivamus elementum</span><br>semper nisi. Aenean vulputate eleifend tellus. Aenean leo ligula,<br>porttitor eu, consequat vitae, eleifend ac, enim.</p>
  </div>

  <div class="printed-name">Daniel Harper</div>
</div>
</body>
</html>
```